Business Cards for a small business advisory (business services)

Professional look. Same as would apply for a lawyer, accountant, or other financial services professional. Please use the logo colors

Target Market(s)

small business owners

Industry/Entity Type

Financial Servics

Contact Information for Business Card

Name: Gavin L. Whitmore, CAIA / Title: Business Advisor / Office #: (718) 294-7716 / Mobile #: (917) 382-5047 / Email: g.whitmore@clearfieldventurepartners.example / Web: www.clearfieldventurepartners.example

Font styles to use
Sans Serif

```html
<!DOCTYPE html>
<html lang="en">
<head>
<meta charset="utf-8">
<title>Clearfield Venture Partners — Business Cards</title>
<link href="https://fonts.googleapis.com/css2?family=Lato:wght@400;700;900&family=Montserrat:wght@600;700&display=swap" rel="stylesheet">
<style>
  :root{
    --navy:#1a3866;
    --green:#8cc63f;
    --white:#ffffff;
    --backdrop:#e6e7ea;
  }
  *{box-sizing:border-box;margin:0;padding:0}
  html,body{width:1200px;height:1122px;overflow:hidden;background:var(--backdrop);font-family:"Lato",sans-serif}
  .card{position:absolute;width:620px;height:354px;border-radius:22px;overflow:hidden;box-shadow:0 10px 26px rgba(0,0,0,.22)}

  /* Back of card */
  .card-back{left:520px;top:120px;background:var(--navy);color:var(--white)}
  .brand-lockup{position:absolute;left:70px;top:120px;display:flex;align-items:center;gap:18px}
  .brand-dot{width:62px;height:62px;border-radius:50%;background:var(--green);flex:none}
  .brand-name{font-family:"Montserrat",sans-serif;font-weight:700;font-size:36px;line-height:1.05;color:var(--white)}
  .tagline{position:absolute;left:150px;top:222px;font-family:"Montserrat",sans-serif;font-weight:600;font-size:10.5px;letter-spacing:.6px;text-transform:uppercase;color:var(--white)}

  /* Front of card */
  .card-front{left:80px;top:610px;background:var(--white)}
  .card-front .waves{position:absolute;inset:0}
  .front-mark{position:absolute;left:58px;top:95px;display:flex;flex-direction:column;align-items:center;gap:10px;width:150px}
  .front-mark .brand-dot{width:84px;height:84px;background:var(--navy)}
  .front-mark .mark-name{font-family:"Lato",sans-serif;font-weight:700;font-size:13px;color:var(--navy);text-align:center;line-height:1.25}
  .holder{position:absolute;right:34px;top:112px;text-align:right}
  .holder-name{font-weight:900;font-size:25px;letter-spacing:.5px;color:var(--navy);text-transform:uppercase}
  .holder-title{font-weight:400;font-size:19px;color:var(--green);margin-top:2px}
  .contacts{position:absolute;right:30px;bottom:22px;list-style:none;text-align:right;color:var(--white)}
  .contacts li{display:flex;justify-content:flex-end;align-items:center;gap:10px;font-size:14.5px;line-height:21px}
  .contacts svg{width:14px;height:14px;flex:none}
</style>
</head>
<body>

<section class="card card-back" aria-label="Card back">
  <div class="brand-lockup">
    <span class="brand-dot"></span>
    <span class="brand-name">Clearfield<br>Venture Partners</span>
  </div>
  <p class="tagline">Your guide to confidently buy or sell a local business today</p>
</section>

<section class="card card-front" aria-label="Card front">
  <svg class="waves" viewBox="0 0 620 354" preserveAspectRatio="none" aria-hidden="true">
    <path d="M70,0 C120,50 220,76 345,78 C280,62 240,28 235,0 Z" fill="var(--green)"/>
    <path d="M0,200 C80,240 160,262 260,252 C360,242 420,205 520,210 C570,212 600,225 620,235 L620,354 L0,354 Z" fill="var(--navy)"/>
  </svg>

  <div class="front-mark">
    <span class="brand-dot"></span>
    <span class="mark-name">Clearfield Venture Partners</span>
  </div>

  <div class="holder">
    <p class="holder-name">Gavin L. Whitmore, CAIA</p>
    <p class="holder-title">Business Advisor</p>
  </div>

  <ul class="contacts">
    <li>(718) 294-7716
      <svg viewBox="0 0 24 24"><path fill="var(--green)" d="M6.6 10.8a15 15 0 0 0 6.6 6.6l2.2-2.2a1 1 0 0 1 1-.25 11.4 11.4 0 0 0 3.6.57 1 1 0 0 1 1 1V20a1 1 0 0 1-1 1A17 17 0 0 1 3 4a1 1 0 0 1 1-1h3.5a1 1 0 0 1 1 1c0 1.25.2 2.45.57 3.6a1 1 0 0 1-.25 1z"/></svg>
    </li>
    <li>(917) 382-5047
      <svg viewBox="0 0 24 24"><rect x="6" y="2" width="12" height="20" rx="2" fill="none" stroke="var(--green)" stroke-width="2.4"/><circle cx="12" cy="18" r="1.4" fill="var(--green)"/></svg>
    </li>
    <li>g.whitmore@clearfieldventurepartners.example
      <svg viewBox="0 0 24 24"><rect x="2" y="5" width="20" height="14" rx="1.5" fill="var(--green)"/><path d="M2.5 6 12 13l9.5-7" fill="none" stroke="var(--navy)" stroke-width="1.6"/></svg>
    </li>
    <li>www.clearfieldventurepartners.example
      <svg viewBox="0 0 24 24"><circle cx="12" cy="12" r="9.5" fill="none" stroke="var(--green)" stroke-width="2.2"/><path d="M2.5 12h19M12 2.5c3 3 3 16 0 19M12 2.5c-3 3-3 16 0 19" fill="none" stroke="var(--green)" stroke-width="1.6"/></svg>
    </li>
  </ul>
</section>

</body>
</html>
```